Banner Ad for our online service

We would like a banner ad for our online service that provides video reviews for people seeking apartments--flatscout.org. We would like you to include our attached logo in the banner and would also like visuals representing our service. The banner should be 300x250 pixels and should include the following text:

-Moving to Boston?
-We review apartments so you don't have to.
-Order now and receive $40 gift card.

We're open to all ideas. Thanks.

```html
<!DOCTYPE html>
<html lang="en">
<head>
<meta charset="utf-8">
<title>FlatScout — Moving to Boston banner</title>
<link rel="stylesheet" href="https://fonts.googleapis.com/css2?family=Archivo+Black&family=Open+Sans:wght@600;700;800&display=swap">
<style>
  :root {
    --stage: #1c1c1c;
    --navy: #1d3160;
    --red: #a3172f;
    --red-dark: #85102a;
    --white: #ffffff;
    --band-top: #f2f2f2;
    --band-bottom: #dcdcdc;
    --ink: #2b2b2b;
    --sky-top: #9fb4cc;
    --sky-mid: #c9d6e4;
    --city: #7d8797;
    --water: #b9c7d6;
    --brand: #e8791e;
  }
  * { margin: 0; padding: 0; box-sizing: border-box; }
  html, body {
    width: 1200px; height: 965px; overflow: hidden;
    background: var(--stage);
  }
  .banner {
    position: absolute; left: 161px; top: 117px;
    width: 880px; height: 734px;
    background: var(--white); overflow: hidden;
  }
  .skyline {
    position: absolute; left: 0; top: 0; width: 880px; height: 310px;
    background: linear-gradient(180deg,
      var(--sky-top) 0%, var(--sky-mid) 25%,
      var(--city) 45%, #8f99a8 62%,
      var(--water) 75%, var(--white) 100%);
  }
  .headline-lead {
    position: absolute; left: 16px; top: 288px;
    font-family: "Archivo Black", sans-serif;
    font-size: 41px; line-height: 45px; color: var(--navy);
    text-transform: uppercase; letter-spacing: -0.5px;
    text-shadow: 0 0 3px var(--white), 0 0 3px var(--white);
  }
  .headline-city {
    position: absolute; left: 282px; top: 270px;
    width: 592px; height: 140px; overflow: visible;
  }
  .headline-city text {
    font-family: "Archivo Black", sans-serif;
    font-size: 158px; fill: var(--red);
    stroke: var(--white); stroke-width: 6px; paint-order: stroke;
  }
  .tagline {
    position: absolute; left: 0; top: 400px; width: 880px;
    text-align: center;
    font-family: "Open Sans", sans-serif; font-weight: 700;
    font-size: 37px; color: var(--red); letter-spacing: -0.5px;
  }
  .steps-band {
    position: absolute; left: 0; top: 454px; width: 880px; height: 176px;
    background: linear-gradient(180deg, var(--band-top), var(--band-bottom));
    display: flex;
  }
  .step {
    flex: 1; display: flex; flex-direction: column; align-items: center;
    padding-top: 22px;
  }
  .step-icon { width: 70px; height: 70px; }
  .step-label {
    margin-top: 20px;
    display: flex; align-items: flex-start; gap: 10px;
    font-family: "Open Sans", sans-serif; font-weight: 600;
    font-size: 26px; line-height: 28px; color: var(--ink);
  }
  .step-number {
    flex: none; width: 28px; height: 28px; border-radius: 50%;
    background: var(--red); color: var(--white);
    font-size: 17px; font-weight: 700; line-height: 28px; text-align: center;
  }
  .step-label .two-line { text-align: center; }
  .brand {
    position: absolute; left: 18px; top: 652px;
    display: flex; align-items: center; gap: 12px;
    font-family: "Open Sans", sans-serif; font-weight: 700;
    font-size: 44px; color: var(--ink); letter-spacing: -1px;
  }
  .brand-dot {
    width: 42px; height: 42px; border-radius: 50%; background: var(--brand);
  }
  .order-button {
    position: absolute; left: 522px; top: 634px;
    width: 343px; height: 82px; border-radius: 10px;
    background: linear-gradient(180deg, var(--red), var(--red-dark));
    color: var(--white); text-align: center;
    font-family: "Open Sans", sans-serif;
    padding-top: 4px;
  }
  .order-button .cta {
    display: block; font-weight: 800; font-size: 40px; line-height: 44px;
  }
  .order-button .offer {
    display: block; font-weight: 700; font-size: 26px; line-height: 28px;
  }
</style>
</head>
<body>
  <div class="banner">
    <div class="skyline" role="img" aria-label="Photo of the Boston city skyline over the harbour"></div>

    <div class="headline-lead">Are you<br>moving to</div>
    <svg class="headline-city" viewBox="0 0 592 140" aria-label="BOSTON">
      <text x="4" y="128" textLength="584" lengthAdjust="spacingAndGlyphs">BOSTON</text>
    </svg>
    <p class="tagline">We review apartments so you don't have to</p>

    <div class="steps-band">
      <div class="step">
        <svg class="step-icon" viewBox="0 0 70 70" aria-hidden="true">
          <rect x="14" y="10" width="42" height="54" rx="3" fill="none" stroke="#333" stroke-width="3"/>
          <rect x="25" y="5" width="20" height="10" rx="2" fill="#333"/>
          <g stroke="#333" stroke-width="3">
            <line x1="22" y1="26" x2="48" y2="26"/>
            <line x1="22" y1="35" x2="48" y2="35"/>
            <line x1="22" y1="44" x2="48" y2="44"/>
            <line x1="22" y1="53" x2="40" y2="53"/>
          </g>
        </svg>
        <div class="step-label"><span class="step-number">1</span><span>Make Your List</span></div>
      </div>
      <div class="step">
        <svg class="step-icon" viewBox="0 0 70 70" aria-hidden="true">
          <circle cx="28" cy="28" r="17" fill="none" stroke="#333" stroke-width="6"/>
          <line x1="41" y1="41" x2="60" y2="60" stroke="#333" stroke-width="9" stroke-linecap="round"/>
        </svg>
        <div class="step-label"><span class="step-number">2</span><span>We Review It</span></div>
      </div>
      <div class="step">
        <svg class="step-icon" viewBox="0 0 70 70" aria-hidden="true">
          <rect x="12" y="6" width="46" height="58" fill="#333"/>
          <rect x="24" y="12" width="22" height="20" fill="#eee"/>
          <rect x="24" y="38" width="22" height="20" fill="#eee"/>
          <g fill="#eee">
            <rect x="15" y="10" width="5" height="5"/><rect x="15" y="22" width="5" height="5"/>
            <rect x="15" y="34" width="5" height="5"/><rect x="15" y="46" width="5" height="5"/>
            <rect x="15" y="56" width="5" height="5"/>
            <rect x="50" y="10" width="5" height="5"/><rect x="50" y="22" width="5" height="5"/>
            <rect x="50" y="34" width="5" height="5"/><rect x="50" y="46" width="5" height="5"/>
            <rect x="50" y="56" width="5" height="5"/>
          </g>
        </svg>
        <div class="step-label"><span class="step-number">3</span><span class="two-line">We Send You<br>The Video</span></div>
      </div>
    </div>

    <div class="brand"><span class="brand-dot"></span><span>FlatScout</span></div>

    <a class="order-button">
      <span class="cta">ORDER NOW</span>
      <span class="offer">Receive a $40 gift card</span>
    </a>
  </div>
</body>
</html>
```